Website will be built in Dot Net Nuke v5 so fonts used need to be system fonts and design needs to be convertible to DNN skins/containers.
There is an existing website www.zestwrapgrill.com.au that we are redesigning with a more updated look based on the below but we are open to deviations or suggestions as to layout.
Site Map
o Home
o Health/Nutrition
o Store Locator
o Products
o Leasing
o Partners
o About Us
o Contact Us
Zesta Design Brief
Colours: Purple and Orange as per attached logo
The website will be purely targeted to the consumer but also allow for franchise enquiry and access for leasing agents. It also needs to portray corporate credibility.
Homepage and a content page will be mocked up with dummy content (have attached some images that can be used)
Design needs to be fresh and funky, young, vibrant with a cool flash section on the homepage
Homepage design requirements:
- Top Left Corner - Zesta Wraps logo
- Next to the logo – a banner with the words “It's how we roll"
- Left Pane (Narrow) – 2 call to action buttons – Franchise Enquiry and Store Locator
- Middle Content Pane – Funky flash area with rotating images that roll away like a kebab to reveal the next image.
- Below Middle Content Pane – Latest News on left and some content on the right
- Right Pane – Logos of clients vertically
Footer - Website Design by KLORA Digital and Privacy Statement, Terms of Use, Login etc that are standard with Dot Net Nuke

```html
<!DOCTYPE html>
<html lang="en">
<head>
<meta charset="utf-8">
<title>Zesta Wraps – It's how we roll</title>
<link href="https://fonts.googleapis.com/css2?family=Arimo:wght@400;700&display=swap" rel="stylesheet">
<style>
:root{
  --purple:#5a1a9a;
  --purple-dark:#3f0f78;
  --purple-text:#4b1487;
  --orange:#ee7a12;
  --orange-dark:#c65f06;
  --white:#ffffff;
  --ink:#222222;
  --grey-line:#d6d6d6;
  --page-bg:#e4e4e6;
}
*{box-sizing:border-box;margin:0;padding:0}
html,body{width:1200px;height:966px;overflow:hidden}
body{font-family:"Arimo",Arial,sans-serif;color:var(--ink);background:linear-gradient(#e9e3ef 540px,var(--page-bg) 700px,#e0e0e2 966px);position:relative}
.top-band{position:absolute;left:0;top:0;width:1200px;height:86px;background:linear-gradient(90deg,var(--purple-dark),var(--purple) 50%,#6b24a8)}
.tagline{position:absolute;left:252px;top:26px;font-size:29px;font-weight:700;color:var(--white)}
.cta{position:absolute;top:28px;height:26px;border-radius:13px;background:var(--orange);color:var(--white);font-size:14px;line-height:26px;text-align:center}
.cta.franchise{left:847px;width:151px}
.cta.locator{left:1006px;width:117px}
.nav-bar{position:absolute;left:0;top:86px;width:1200px;height:40px;background:var(--orange)}
.main-nav{position:absolute;left:256px;top:94px;display:flex;font-size:17px;color:var(--white)}
.main-nav span{white-space:nowrap}
.main-nav .sep{margin:0 13px}
.main-nav .current{color:var(--purple-text);font-weight:700}
.logo{position:absolute;left:70px;top:0;width:164px;height:165px;z-index:2}
.hero{position:absolute;left:0;top:126px;width:1200px;height:430px;
  background:
    linear-gradient(180deg,rgba(233,227,239,0) 70%,#e9e3ef 100%),
    linear-gradient(90deg,#5b3a66 0%,#8a5a4a 25%,#6e4f6a 45%,#9a6a48 65%,#7b5a84 85%,#8c6fa6 100%),
    #6a4a70}
.slide-dots{position:absolute;top:397px;left:1061px;display:flex;gap:7px}
.slide-dots i{width:19px;height:19px;border-radius:50%;background:#e8e8e8;border:1px solid #bbb}
.slide-dots i.on{background:var(--orange)}
.panel{position:absolute;left:67px;top:428px;width:1077px;height:462px;background:var(--white);border-radius:0 24px 0 0}
.intro{position:absolute;left:77px;top:439px;width:1058px;height:83px;background:linear-gradient(90deg,var(--orange-dark),#d36a0a);border-radius:0 18px 0 0;color:var(--white);padding:13px 14px;font-size:15.5px;line-height:18px}
.intro strong{display:block;font-size:16px}
.stripe{position:absolute;left:77px;top:522px;width:1058px;height:22px;background:repeating-linear-gradient(135deg,#bdbdbd 0 2px,#e4e4e4 2px 5px)}
h2{font-size:19px;color:var(--purple-text);font-weight:700}
.news{position:absolute;left:86px;top:564px;width:308px;font-size:14.5px;line-height:18px}
.news h2{display:flex;align-items:center;gap:10px;margin-bottom:9px}
.news p{padding-bottom:10px}
.news .rule{border-top:1px dotted #bbb;margin-bottom:10px}
.col-divider{position:absolute;left:408px;top:552px;width:2px;height:230px;background:linear-gradient(#ececec,#f8f8f8)}
.welcome{position:absolute;left:430px;top:568px;width:700px;font-size:14.5px;line-height:18.4px}
.welcome h2{margin-bottom:10px}
.welcome p{margin-bottom:18px}
.clients-rule{position:absolute;left:84px;top:787px;width:1040px;border-top:1px solid var(--grey-line)}
.clients-tab{position:absolute;left:84px;top:787px;width:23px;height:89px;background:var(--purple-text);color:var(--white);font-size:13px;writing-mode:vertical-rl;transform:rotate(180deg);text-align:center;line-height:23px}
.client-list{position:absolute;left:120px;top:822px;width:998px;display:flex;justify-content:space-between;align-items:center;font-size:16px;font-weight:700}
.client-list span{white-space:nowrap}
.footer{position:absolute;left:71px;top:905px;font-size:14px;line-height:20px;color:var(--ink)}
.footer u{text-decoration:underline}
.social{position:absolute;right:108px;top:916px;display:flex;gap:14px;font-size:13px;color:var(--ink)}
.social span{display:flex;align-items:center;gap:5px;white-space:nowrap}
.social i{width:16px;height:16px;border-radius:2px;background:#3b66a8}
.social .chirp i{background:#4fb3dd}
</style>
</head>
<body>
<div class="top-band"></div>
<div class="tagline">It's how we roll</div>
<div class="cta franchise">Franchise Enquiry</div>
<div class="cta locator">Store Locator</div>
<div class="nav-bar"></div>
<nav class="main-nav">
  <span class="current">Home</span><span class="sep">|</span>
  <span>Health/Nutrition</span><span class="sep">|</span>
  <span>Store Locator</span><span class="sep">|</span>
  <span>Products</span><span class="sep">|</span>
  <span>Leasing</span><span class="sep">|</span>
  <span>Partners</span><span class="sep">|</span>
  <span>About Us</span><span class="sep">|</span>
  <span>Contact Us</span>
</nav>
<div class="hero" role="img" aria-label="Photo of a busy wrap shop counter with grills, drinks fridges and menu boards"></div>
<svg class="logo" viewBox="0 0 164 165" aria-label="Zesta Wraps">
  <path d="M0 0H164V118L82 165L0 118Z" fill="#d8690a"/>
  <text x="82" y="92" text-anchor="middle" font-family="Arimo, Arial, sans-serif" font-weight="700" font-size="24" fill="#4b1487">Zesta Wraps</text>
</svg>
<div class="slide-dots"><i class="on"></i><i></i><i></i></div>
<div class="panel"></div>
<div class="intro">
  <strong>Lorem ipsum dolor sit amet, consectetur adipiscing elit. Proin est tortor, pulvinar vel ullam corperut</strong>
  Porttitor non ante. Nam bibendum mi sit amet ipsum pulvinar volutpat. Aenean blandit iaculis tellus, non dapibus est vehicula n. Sed a neque metus luctus ligula. Cras id neque velit, id pulvinar velit. Integer eu nisi at massa consectetur adipiscing elit.
</div>
<div class="stripe"></div>
<section class="news">
  <h2><svg width="17" height="17" viewBox="0 0 17 17"><circle cx="8" cy="8" r="6" fill="none" stroke="#888" stroke-width="2"/><path d="M3 13L1 16" stroke="#888" stroke-width="2"/></svg>What's New</h2>
  <p>Lorem ipsum dolor sit amet, consectetur adipi tyu scing elit. Proin est tortor, pulvinar vel uam ishjuk&nbsp; corper ut, porttitor non is&nbsp; ante.</p>
  <div class="rule"></div>
  <p>Nabib uiyhd sec endum mi sit amet ipsum pulvinar volut patam bib uiyhd endum mi sit amet ipsm pulvinar volutpat. Endum mi sit amet ipsum pulvinar volut patam.</p>
</section>
<div class="col-divider"></div>
<section class="welcome">
  <h2>Welcome to Zesta Wraps</h2>
  <p>In 1989, Mr Sam Dorell launched the first Zesta Wrap (ZW) shop in Parkway Plaza Shopping Center, Loganholme Queensland. Queenslanders had not yet seen nor heard of a kebab. After a fierce sampling exercise, Queenslanders embraced Zesta Wraps. It was a roaring success. To this day Zesta at Parkway Plaza, is recognised as one of the most successful kebab retail shops in the country.</p>
  <p>Within 3 years Zesta Wraps was operating in 4 locations between the Gold Coast and Brisbane. Lorem ipsum dolor sit amet, consectetur adipi tyu scing elit. Proin est tortor, pulvinar vel uam ishjuk corper ut, porttitor non is&nbsp; ante.</p>
</section>
<div class="clients-rule"></div>
<div class="clients-tab">Our Clients</div>
<div class="client-list">
  <span style="color:#1c6b3a">Northline</span>
  <span style="color:#2a62b0">CareWell</span>
  <span style="color:#6a9a2a">LimeGroup</span>
  <span style="color:#1f5a4a">CONCORA</span>
  <span style="color:#b0182a">Star Diner</span>
  <span style="color:#666">forwardly</span>
  <span style="color:#222">TRACKCLUB</span>
  <span style="color:#d4141c">PETROLUX</span>
  <span style="color:#111">KESTREL</span>
</div>
<footer class="footer">
  <div>T: +61 7 3000 1234&nbsp; | &nbsp;F: +61 7 3000 1299&nbsp; | &nbsp;E: info@zestawraps.com.au</div>
  <div><u>Terms Of Use</u>&nbsp; | &nbsp;<u>Privacy Statement</u>&nbsp;&nbsp; Copyright © 2011 Zesta Wraps. All rights reserved.</div>
</footer>
<div class="social"><span><i></i>Friendly</span><span class="chirp"><i></i>Chirper</span></div>
</body>
</html>
```